Personal Tax Specialists Banner

We need banner adverts for a personal tax firm. We specialise in Luxembourg, US and UK personal taxation. The banner should be modern, cool, simple and illustrated.

Banner should highlight "Personal Taxation Specialists" and the countries that we specialise in, "Luxembourg", "US" and "UK".

Target Market(s)

Individuals looking for assistance with tax return preparation.

Industry/Entity Type

Finance And Accounting

Colors

Designer to choose colors to be used in the design.

Requirements
Must have
• Output in GIF.
• The main banner size is 980 x 120 and some smaller square banners (300 x 300)
• Button to link back to website www.pelvorytax.com
Nice to have
• We would like an illustrated design if possible.

```html
<!DOCTYPE html>
<html lang="en">
<head>
<meta charset="utf-8">
<title>Pelvory Tax &amp; Consulting – Banners</title>
<link href="https://fonts.googleapis.com/css2?family=Oswald:wght@500&family=Open+Sans:wght@400;600&display=swap" rel="stylesheet">
<style>
  :root {
    --maroon: #6f0b2f;
    --maroon-dark: #56071f;
    --silver: #f1f1f1;
    --photo-light: #d6d6d6;
    --photo-dark: #8d8d8d;
    --gold-light: #f0c987;
    --gold-mid: #cf9a4a;
    --gold-dark: #a86f28;
    --button-text: #3a2a1c;
    --page: #e6e8eb;
    --white: #ffffff;
    --ring: #9a9a9a;
  }
  * { margin: 0; padding: 0; box-sizing: border-box; }
  html, body { width: 1200px; height: 1200px; overflow: hidden; background: var(--page); }
  .canvas { position: relative; width: 1200px; height: 1200px; background: var(--page); }

  .banner { position: absolute; overflow: hidden; }
  .banner-shapes { position: absolute; inset: 0; width: 100%; height: 100%; }
  .banner > * { position: absolute; }

  .banner--square { left: 348px; top: 134px; width: 522px; height: 520px; }
  .banner--leaderboard { left: 16px; top: 786px; width: 1168px; height: 140px; }

  .headline {
    font-family: "Oswald", "Arial Narrow", sans-serif;
    font-weight: 500;
    color: var(--white);
    text-transform: uppercase;
    text-shadow: 2px 3px 4px rgba(0,0,0,.55);
    letter-spacing: 0.3px;
  }
  .banner--square .headline { left: 36px; top: 178px; font-size: 50px; line-height: 55px; }
  .banner--leaderboard .headline { left: 382px; top: 6px; font-size: 33px; line-height: 39px; }

  .scales-illustration {
    background: radial-gradient(ellipse at 50% 55%, rgba(215,165,80,.9) 0%, rgba(190,140,60,.55) 40%, rgba(160,160,160,0) 72%);
  }
  .banner--square .scales-illustration { left: 258px; top: 126px; width: 228px; height: 174px; }
  .banner--leaderboard .scales-illustration { left: 198px; top: 10px; width: 162px; height: 122px; }

  .brand { display: flex; align-items: center; gap: 14px; color: var(--maroon); font-family: "Open Sans", Arial, sans-serif; font-weight: 600; }
  .brand-mark { border: 3px solid var(--ring); border-radius: 50%; flex: none; }
  .brand-name { line-height: 1; text-transform: uppercase; }
  .brand-name span { display: block; }
  .banner--square .brand { left: 14px; top: 20px; }
  .banner--square .brand-mark { width: 60px; height: 60px; }
  .banner--square .brand-name .name { font-size: 34px; letter-spacing: 1px; }
  .banner--square .brand-name .sub { font-size: 13px; margin-top: 6px; letter-spacing: 0.5px; }
  .banner--leaderboard .brand { left: 626px; top: 86px; gap: 8px; }
  .banner--leaderboard .brand-mark { width: 34px; height: 34px; border-width: 2px; }
  .banner--leaderboard .brand-name .name { font-size: 24px; letter-spacing: 0.5px; }
  .banner--leaderboard .brand-name .sub { font-size: 10px; margin-top: 3px; }

  .countries { display: flex; }
  .countries svg { display: block; }
  .banner--square .countries { left: 50px; top: 456px; gap: 6px; }
  .banner--square .countries svg { width: 44px; height: 44px; }
  .banner--leaderboard .countries { left: 398px; top: 92px; gap: 6px; }
  .banner--leaderboard .countries svg { width: 40px; height: 40px; }

  .site-button {
    display: flex; align-items: center; justify-content: center;
    font-family: "Open Sans", Arial, sans-serif; font-weight: 400;
    color: var(--button-text); text-decoration: none;
    background: linear-gradient(180deg, var(--gold-light) 0%, var(--gold-mid) 50%, var(--gold-dark) 100%);
    border: 1px solid #f7dfae; border-radius: 5px;
    box-shadow: 0 2px 4px rgba(0,0,0,.35);
  }
  .banner--square .site-button { left: 234px; top: 448px; width: 264px; height: 50px; font-size: 21px; }
  .banner--leaderboard .site-button { left: 908px; top: 50px; width: 222px; height: 40px; font-size: 18px; }
</style>
</head>
<body>
<svg width="0" height="0" style="position:absolute" aria-hidden="true">
  <defs>
    <clipPath id="flag-clip"><circle cx="20" cy="20" r="17"/></clipPath>
    <symbol id="flag-lu" viewBox="0 0 40 40">
      <g clip-path="url(#flag-clip)">
        <rect width="40" height="14" fill="#e8283a"/>
        <rect y="14" width="40" height="12" fill="#ffffff"/>
        <rect y="26" width="40" height="14" fill="#19a2dc"/>
      </g>
      <circle cx="20" cy="20" r="17.5" fill="none" stroke="#ffffff" stroke-width="3"/>
    </symbol>
    <symbol id="flag-us" viewBox="0 0 40 40">
      <g clip-path="url(#flag-clip)">
        <rect width="40" height="40" fill="#ffffff"/>
        <rect y="3" width="40" height="3" fill="#c8202f"/>
        <rect y="9" width="40" height="3" fill="#c8202f"/>
        <rect y="15" width="40" height="3" fill="#c8202f"/>
        <rect y="21" width="40" height="3" fill="#c8202f"/>
        <rect y="27" width="40" height="3" fill="#c8202f"/>
        <rect y="33" width="40" height="3" fill="#c8202f"/>
        <rect width="20" height="21" fill="#2a3f86"/>
      </g>
      <circle cx="20" cy="20" r="17.5" fill="none" stroke="#ffffff" stroke-width="3"/>
    </symbol>
    <symbol id="flag-uk" viewBox="0 0 40 40">
      <g clip-path="url(#flag-clip)">
        <rect width="40" height="40" fill="#23367d"/>
        <path d="M0 0L40 40M40 0L0 40" stroke="#ffffff" stroke-width="8"/>
        <path d="M0 0L40 40M40 0L0 40" stroke="#c8202f" stroke-width="3"/>
        <path d="M20 0V40M0 20H40" stroke="#ffffff" stroke-width="11"/>
        <path d="M20 0V40M0 20H40" stroke="#c8202f" stroke-width="6"/>
      </g>
      <circle cx="20" cy="20" r="17.5" fill="none" stroke="#ffffff" stroke-width="3"/>
    </symbol>
    <linearGradient id="photo-fill" x1="0" y1="0" x2="1" y2="1">
      <stop offset="0" stop-color="#e2e2e2"/>
      <stop offset="0.55" stop-color="#b4b4b4"/>
      <stop offset="1" stop-color="#cfcfcf"/>
    </linearGradient>
    <linearGradient id="maroon-fill" x1="0" y1="0" x2="0" y2="1">
      <stop offset="0" stop-color="#7a0f35"/>
      <stop offset="1" stop-color="#5e0823"/>
    </linearGradient>
    <linearGradient id="silver-fill" x1="0" y1="0" x2="1" y2="0">
      <stop offset="0" stop-color="#ffffff"/>
      <stop offset="0.5" stop-color="#d9d9d9"/>
      <stop offset="1" stop-color="#ffffff"/>
    </linearGradient>
  </defs>
</svg>

<main class="canvas">

  <section class="banner banner--square" aria-label="Square banner">
    <svg class="banner-shapes" viewBox="0 0 435 433" preserveAspectRatio="none" aria-hidden="true">
      <rect width="435" height="433" fill="#ffffff"/>
      <polygon points="175,98 435,36 435,56" fill="url(#maroon-fill)"/>
      <polygon points="0,112 435,62 435,268 0,352" fill="url(#photo-fill)"/>
      <polygon points="0,352 435,268 435,282 0,366" fill="url(#silver-fill)"/>
      <polygon points="0,366 435,282 435,433 0,433" fill="url(#maroon-fill)"/>
    </svg>
    <div class="brand">
      <span class="brand-mark"></span>
      <p class="brand-name"><span class="name">Pelvory</span><span class="sub">Tax &amp; Consulting</span></p>
    </div>
    <div class="scales-illustration" role="img" aria-label="Golden scales of justice"></div>
    <h1 class="headline">Personal<br>Taxation<br>Specialists</h1>
    <div class="countries" aria-label="Luxembourg, US and UK">
      <svg role="img" aria-label="Luxembourg"><use href="#flag-lu"/></svg>
      <svg role="img" aria-label="United States"><use href="#flag-us"/></svg>
      <svg role="img" aria-label="United Kingdom"><use href="#flag-uk"/></svg>
    </div>
    <a class="site-button" href="#">www.pelvorytax.com</a>
  </section>

  <section class="banner banner--leaderboard" aria-label="Leaderboard banner">
    <svg class="banner-shapes" viewBox="0 0 974 117" preserveAspectRatio="none" aria-hidden="true">
      <rect width="974" height="117" fill="url(#maroon-fill)"/>
      <polygon points="95,0 110,0 152,117 137,117" fill="url(#silver-fill)"/>
      <polygon points="110,0 655,0 430,117 152,117" fill="url(#photo-fill)"/>
      <polygon points="655,0 698,0 722,117 430,117" fill="#f7f7f7"/>
      <polygon points="698,0 712,0 736,117 722,117" fill="url(#silver-fill)"/>
    </svg>
    <div class="scales-illustration" role="img" aria-label="Golden scales of justice"></div>
    <h2 class="headline">Personal Taxation<br>Specialists</h2>
    <div class="countries" aria-label="Luxembourg, US and UK">
      <svg role="img" aria-label="Luxembourg"><use href="#flag-lu"/></svg>
      <svg role="img" aria-label="United States"><use href="#flag-us"/></svg>
      <svg role="img" aria-label="United Kingdom"><use href="#flag-uk"/></svg>
    </div>
    <div class="brand">
      <span class="brand-mark"></span>
      <p class="brand-name"><span class="name">Pelvory</span><span class="sub">Tax &amp; Consulting</span></p>
    </div>
    <a class="site-button" href="#">www.pelvorytax.com</a>
  </section>

</main>
</body>
</html>
```